Wordpress Design Project (Tobwin)

We need a wordpress design for an established auction and real estate company based in Virginia. The winning design will incorporate the colors of logo (red and black) creatively with an accent color in a very professional and clean layout.

Industry/Entity Type

Real Estate

Requirements
Must have
• We will require winning designer to provide a layered PSD (Adobe photoshop) concept file, along with any non-standard font files used.

Horizontal Navigation menu with these links:
Home - Upcoming Auctions - Past Auctions - For Sale- Consignments - About Us - Highlights - Contact Us

A slideshow element on the home page using the placeholder image provided.

Sidebar widgets to be included are: Email sign-up form - Featured Auctions - Featured Assets for Sale (see attached for visual of these widgets)

attached logos in footer with company contact info

```html
<!DOCTYPE html>
<html lang="en">
<head>
<meta charset="utf-8">
<title>Tobwin Enterprises — Auctions &amp; Real Estate</title>
<link href="https://fonts.googleapis.com/css2?family=Arimo:wght@400;700&family=Open+Sans:wght@400;600;700&display=swap" rel="stylesheet">
<style>
:root{
  --red:#c8231c;
  --red-deep:#8e1410;
  --red-dark:#5c0c0a;
  --black:#111;
  --charcoal:#2b2b2b;
  --grey-bg:#3a3a3a;
  --white:#fff;
  --text:#222;
  --muted:#555;
  --sky:#9fb3c6;
  --water:#6f7f8c;
  --grass:#6f8a3a;
}
*{margin:0;padding:0;box-sizing:border-box}
html,body{width:1034px;height:1200px;overflow:hidden}
body{font-family:"Arimo",Arial,sans-serif;color:var(--text);background:var(--grey-bg);position:relative}
.abs{position:absolute}
.band-top{left:0;top:0;width:1034px;height:61px;background:repeating-linear-gradient(45deg,#262626 0 2px,#1c1c1c 2px 4px)}
.band-nav{left:0;top:61px;width:1034px;height:63px;background:#f6f6f6;border-bottom:1px solid #ddd}
.band-hero{left:0;top:124px;width:1034px;height:241px;background:radial-gradient(ellipse at 50% 40%,#c42a22 0%,#8e1410 70%,#6a0e0b 100%)}
.band-body{left:0;top:365px;width:1034px;height:627px;background:repeating-linear-gradient(45deg,#3d3d3d 0 2px,#343434 2px 4px)}
.band-foot{left:0;top:992px;width:1034px;height:208px;background:radial-gradient(ellipse at 50% 0%,#8e1410 0%,#5e0d0a 60%,#3c0806 100%)}
.top-links{right:129px;top:24px;color:#fff;font-size:12px}
.logo-box{left:131px;top:16px;width:260px;height:108px;background:linear-gradient(#fff,#eee);border-radius:10px 10px 0 0;box-shadow:0 0 8px rgba(0,0,0,.3);display:flex;align-items:center;justify-content:center;gap:10px}
.logo-mark{width:34px;height:34px;background:var(--red)}
.logo-name{font-family:"Open Sans",sans-serif;font-weight:700;font-size:30px;color:var(--red-dark);line-height:1}
.main-nav{left:412px;top:78px;display:flex;align-items:center;font-size:12px;color:#111}
.main-nav a{color:#111;text-decoration:none;display:block;padding:0 12px;line-height:33px}
.main-nav a.current{background:linear-gradient(#333,#000);color:#fff;border-radius:3px}
.hero{left:129px;top:131px;width:550px;height:199px;background:linear-gradient(#b8c8d8 0%,#9fb3c6 24%,#4f6a48 30%,#6f7f8c 34%,#7b8a96 62%,#6f8a3a 80%,#4b5f26 100%)}
.dots{left:145px;top:306px;display:flex;gap:4px}
.dots span{width:14px;height:14px;border-radius:50%;background:#000;border:2px solid #fff}
.dots span.on{background:var(--red)}
.signup{left:679px;top:131px;width:227px;height:199px;background:linear-gradient(#1a1a1a,#000)}
.signup h2{position:absolute;left:44px;top:8px;font-family:"Open Sans",sans-serif;font-weight:600;font-size:20px;color:#b9f0b0}
.signup .ico{position:absolute;left:13px;top:12px;width:24px;height:20px;background:#dfe6ef;border-radius:3px}
.field{position:absolute;left:12px;width:194px;height:31px;background:#fff;border-radius:6px;border:1px solid #999;font-family:"Open Sans",sans-serif;font-size:12.5px;color:#444;padding:7px 10px}
.sub-btn{position:absolute;left:12px;top:125px;width:205px;height:62px;background:var(--red);border-radius:10px;padding:5px}
.sub-btn span{display:flex;align-items:center;justify-content:center;height:100%;background:linear-gradient(#3a3a3a,#000);border-radius:8px;color:#fff;font-family:"Open Sans",sans-serif;font-weight:700;font-size:16px}
.container{left:129px;top:337px;width:776px;height:675px;background:#fff;border-radius:8px}
.panel{background:#fff;border:1px solid #ccc;border-radius:7px;overflow:hidden}
.panel-head{height:38px;color:#fff;font-size:17px;padding:10px 12px;line-height:18px}
.head-red{background:linear-gradient(#c8231c,#7e100d)}
.head-black{background:linear-gradient(#3a3a3a,#000)}
.featured{left:141px;top:346px;width:513px;height:523px}
.lot-title{position:absolute;left:15px;font-weight:700;font-size:13.5px;color:#111}
.thumb{position:absolute;left:12px;width:138px;height:93px;background:#ccc;padding:4px}
.thumb div{width:100%;height:100%;background:linear-gradient(#c6d7e6 0%,#c6d7e6 30%,#8e5a45 45%,#7a4a3a 65%,#5f8a32 75%,#4f7a28 100%)}
.lot-body{position:absolute;left:158px;width:345px;font-size:9.5px;line-height:17px}
.lot-body .kind{color:var(--red);font-size:12px;margin-bottom:2px}
.lot-body b{font-weight:700}
.lot-body .desc{margin-top:3px;line-height:17px;font-size:9.5px}
.btn-dark{position:absolute;height:29px;width:141px;background:linear-gradient(#3a3a3a,#000);border:1px solid #000;border-radius:3px;color:#fff;font-family:"Open Sans",sans-serif;font-size:12px;display:flex;align-items:center;gap:12px;padding-left:10px;box-shadow:inset 0 0 0 1px #555}
.btn-dark i{width:14px;height:12px;background:#ddd;display:block}
.rule{position:absolute;left:20px;width:475px;height:1px;background:linear-gradient(90deg,transparent,#bbb,transparent);box-shadow:0 3px 6px rgba(0,0,0,.15)}
.upcoming{left:677px;top:346px;width:220px;height:318px}
.side-body{padding:12px 13px;font-size:9.5px;line-height:17px}
.side-body .label{color:var(--red);font-weight:700}
.btn-red{position:absolute;height:29px;width:140px;background:linear-gradient(#c8231c,#7e100d);border:1px solid #5c0c0a;border-radius:3px;color:#fff;font-family:"Open Sans",sans-serif;font-size:12px;display:flex;align-items:center;justify-content:center}
.testimonials{left:677px;top:674px;width:220px;height:197px}
.quote{color:#b0150f;font-weight:700;font-size:9.5px;line-height:17px}
.partners{left:311px;top:936px;display:flex;gap:12px;align-items:center}
.partners span{display:block;background:#ddd}
.foot-links{font-size:10px;color:#fff;line-height:19.5px}
.foot-contact{left:412px;top:1052px;color:#fff;font-size:10px;line-height:19px}
.foot-contact .phone{font-size:19px;line-height:24px}
.news{left:658px;top:1056px;width:245px;height:23px;background:linear-gradient(#d42a22,#a4130f);border-radius:12px;border:2px solid #e24a40;color:#fff;font-size:10px;font-weight:700;padding:3px 14px}
.news span{position:absolute;right:3px;top:2px;width:78px;height:15px;background:#111;border-radius:8px;font-size:8px;padding:2px 8px}
.follow{left:764px;top:1120px;color:#fff;font-size:9px;font-weight:700;display:flex;gap:8px;align-items:center}
.follow i{width:13px;height:13px;background:#3b7fc4;display:block;border-radius:2px}
.follow i.o{background:#e8862b}
.foot-rule{left:129px;top:1157px;width:776px;height:1px;background:#7a2a26}
.copy{left:129px;top:1175px;color:#fff;font-size:9px}
.copy-links{right:129px;top:1175px;color:#fff;font-size:9px}
</style>
</head>
<body>
<div class="abs band-top"></div>
<div class="abs band-nav"></div>
<div class="abs band-hero"></div>
<div class="abs band-body"></div>
<div class="abs band-foot"></div>

<div class="abs top-links">About Us / Contact Us</div>
<div class="abs logo-box"><span class="logo-mark"></span><span class="logo-name">Tobwin</span></div>
<nav class="abs main-nav">
  <a class="current">Home</a><a>Upcoming Auctions</a><a style="padding-left:18px">Past Auctions</a><a style="padding-left:18px">For Sale</a><a style="padding-left:18px">Consignments</a><a>Highlights</a>
</nav>

<div class="abs hero" role="img" aria-label="Slideshow photo of a calm river with a wooden pier and green shoreline"></div>
<div class="abs dots"><span class="on"></span><span></span><span></span><span></span></div>

<div class="abs signup">
  <span class="ico"></span><h2>Sign Up</h2>
  <div class="field" style="top:42px">Enter your Name</div>
  <div class="field" style="top:81px">Enter your Email Address</div>
  <div class="sub-btn"><span>SUBSCRIBE</span></div>
</div>

<div class="abs container"></div>

<section class="abs panel featured">
  <div class="panel-head head-red">Featured Auctions</div>
  <div class="lot-title" style="top:63px">REAL ESTATE AND CONSIGNMENT</div>
  <div class="thumb" style="top:88px"><div role="img" aria-label="Photo of a brick country house with a green lawn"></div></div>
  <div class="lot-body" style="top:88px">
    <div class="kind">LIVE ON-SITE AUCTION</div>
    <div><b>Begins :</b> Wed, April 10, 2013 at 2.00 PM</div>
    <div><b>Location :</b> 1180, Willow Bend Lane, Cedar Hollow, 23150</div>
    <div class="desc">Lorem ipsum dolor sit amet consecutor. Lorem ipsum dolor sit. Lorem ipsum dolor sit amet consecutor. Lorem ipsum dolor. Lorem ipsum dolor sit amet consecutor. Lorem ipsum dolor sit. Lorem ipsum dolor</div>
  </div>
  <div class="btn-dark" style="left:158px;top:203px"><i></i>More Details</div>
  <div class="btn-dark" style="left:305px;top:203px"><i></i>Photo Galleries</div>
  <div class="rule" style="top:256px"></div>

  <div class="lot-title" style="top:292px">REAL ESTATE AND CONSIGNMENT</div>
  <div class="thumb" style="top:317px"><div role="img" aria-label="Photo of a brick country house with a green lawn"></div></div>
  <div class="lot-body" style="top:317px">
    <div class="kind">LIVE ON-SITE AUCTION</div>
    <div><b>Begins :</b> Wed, April 10, 2013 at 2.00 PM</div>
    <div><b>Location :</b> 1180, Willow Bend Lane, Cedar Hollow, 23150</div>
    <div class="desc">Lorem ipsum dolor sit amet consecutor. Lorem ipsum dolor sit. Lorem ipsum dolor sit amet consecutor. Lorem ipsum dolor. Lorem ipsum dolor sit amet consecutor. Lorem ipsum dolor sit. Lorem ipsum dolor</div>
  </div>
  <div class="btn-dark" style="left:158px;top:432px"><i></i>More Details</div>
  <div class="btn-dark" style="left:305px;top:432px"><i></i>Photo Galleries</div>
</section>

<aside class="abs panel upcoming">
  <div class="panel-head head-black">Upcoming Auctions</div>
  <div class="side-body">
    <div style="font-weight:700;font-size:11px">Session 1: Multi Estate and Consignment</div>
    <div style="margin:12px auto 14px;width:137px;height:92px;background:#ccc;padding:4px"><div role="img" aria-label="Photo of a silver minivan parked on a lot" style="width:100%;height:100%;background:linear-gradient(#7e9bc4 0%,#9fb0c0 35%,#b9bcc0 60%,#555 100%)"></div></div>
    <div style="font-weight:700"><span class="label">Start Date/Time :</span> Wed, April 10, 2013 at 2.00 PM</div>
    <div style="font-weight:700"><span class="label">Location :</span> 1180, Willow Bend Lane, Cedar Hollow, 23150</div>
  </div>
  <div class="btn-red" style="left:36px;top:271px">More Details</div>
</aside>

<aside class="abs panel testimonials">
  <div class="panel-head head-black">Client Testimonials</div>
  <div class="side-body">
    <div class="quote">Lorem ipsum dolor sit amet consecutor. Lorem ipsum dolor sit. Lorem ipsum dolor sit amet consecutor. Lorem ipsum dolor. Lorem ipsum dolor sit amet consecutor. Lorem ipsum dolor sit. Lorem ipsum dolor</div>
  </div>
  <div class="btn-red" style="left:43px;top:147px">Read More</div>
</aside>

<div class="abs" style="left:160px;top:912px;width:714px;height:1px;background:linear-gradient(90deg,transparent,#ccc,transparent);box-shadow:0 3px 6px rgba(0,0,0,.12)"></div>
<div class="abs partners" aria-label="Partner associations">
  <span style="width:34px;height:40px;background:#222"></span>
  <span style="width:80px;height:40px;background:#555"></span>
  <span style="width:78px;height:28px;background:#666"></span>
  <span style="width:60px;height:60px;border-radius:50%;background:#2a3f8a;border:3px solid #c8231c"></span>
  <span style="width:125px;height:50px;background:linear-gradient(90deg,#d9231c,#e6c41e)"></span>
</div>

<div class="abs foot-links" style="left:131px;top:1052px">HOME<br>UPCOMING AUCTIONS<br>PAST AUCTIONS</div>
<div class="abs foot-links" style="left:258px;top:1052px">FOR SALE<br>CONSIGNMENTS<br>HIGHLIGHTS</div>
<div class="abs foot-contact">Street Name, City, ZIP Code:110096<br>hello@tobwinenterprises.com<div class="phone">555-018-2740</div><div style="padding-left:3px">Monday-Friday 9-5pm</div></div>
<div class="abs news">Email Address<span>SIGN UP ▸</span></div>
<div class="abs follow">Follow us on <i></i><i></i><i class="o"></i><i></i></div>
<div class="abs foot-rule"></div>
<div class="abs copy">© 2013 Tobwin Enterprises. All Rights Reserved.</div>
<div class="abs copy-links">About Us &nbsp;I&nbsp; Contact Us</div>
</body>
</html>
```